Dr Mira Thalen, Orthopaedic Hand Surgeon

I am an orthopaedic hand surgeon and need business cards that reflect the surgery I do. I operate on bones, ligaments, tendons, and soft tissues. I can do microsurgery (surgery under an operating microscope) - including connecting ends of cut nerves and arteries in the fingers together. As an orthopaedic surgeon, I also fix fractures and manage orthopaedic trauma in the rest of the body. I favour black as a colour, and have some pictures of hand X-rays that you can use in the design, if you think that would look good (feel free to crop).
Updates

Hi all. Thank you for all your submissions so far. Please note that I have updated my project brief. I would like to emphasise that use of the logos that I have provided is optional, and if used, I would very much prefer the logo not to dominate the card, but add to the overall aesthetic of the card. Warm regards, Mira

Target Market(s)

Referring medical practitioners, hand therapists, patients

Industry/Entity Type

Healthcare

Contact Information for Business Card

Dr Mira Thalen
Orthopaedic Hand Surgeon
MBBS BSc (Med), MIntPH (Merit), FCWES (Ortho), FUPelV

Font styles to use
Serif

Colors

Designer to choose colors to be used in the design.

Requirements
Must have
• Space for:
• 2 addresses (a PO Box Address and a consulting suite address) - to be confirmed
• 1 phone number - to be confirmed
Nice to have
• Please choose one of the FCWES logos (I included 3 - colour, black reverse, and greyscale); if you include this in the design, IT SHOULD NOT DOMINATE THE CARD, but be smaller and more discreet.
• I have also attached the FUPelV logo (colour and greyscale); if you choose to include this in the design, IT SHOULD NOT DOMINATE THE CARD, but be smaller and more discreet.
• I would love to be able to update details on the card as time goes on, and thus would like to own the template for the card as well.
• Also I would love discussion with regard to any changes on the card, if I am not completely happy with the design, and would like to discuss things such as ease of printing, finish on the cards (matte, polish) etc.
Should not have
• I don't like the card to look too crowded

```html
<!DOCTYPE html>
<html lang="en">
<head>
<meta charset="utf-8">
<title>Dr Mira Thalen – Business Card</title>
<link rel="stylesheet" href="https://fonts.googleapis.com/css2?family=Montserrat:wght@300;400;600&display=swap">
<style>
  :root {
    --backdrop: #e6e6e6;
    --card: #f2f2f2;
    --band: #000000;
    --ink: #111111;
    --reverse: #f2f2f2;
    --xray-light: #8a8a8a;
    --xray-dark: #0b0b0b;
  }
  html, body {
    margin: 0;
    width: 1200px;
    height: 798px;
    overflow: hidden;
    background: var(--backdrop);
    font-family: "Montserrat", sans-serif;
  }
  .card {
    position: absolute;
    left: 40px;
    top: 79px;
    width: 1120px;
    height: 640px;
    background: var(--card);
    overflow: hidden;
  }
  .card__band {
    position: absolute;
    left: 0; top: 0;
    width: 100%;
    height: 323px;
    background: var(--band);
  }
  .identity {
    position: absolute;
    left: 71px;
    top: 92px;
    color: var(--reverse);
  }
  .identity__name {
    margin: 0;
    font-weight: 600;
    font-size: 53px;
    line-height: 1;
    letter-spacing: 1px;
    text-transform: uppercase;
  }
  .identity__role {
    margin: 12px 0 0;
    font-weight: 300;
    font-size: 30px;
    line-height: 1;
    letter-spacing: 1.5px;
    text-transform: uppercase;
  }
  .identity__credentials {
    margin: 26px 0 0;
    font-weight: 400;
    font-size: 16px;
    font-variant: small-caps;
    letter-spacing: 0.3px;
  }
  .xray {
    position: absolute;
    left: 603px;
    top: 12px;
    width: 386px;
    height: 311px;
    background: radial-gradient(ellipse at 25% 55%, var(--xray-light) 0%, #3a3a3a 30%, transparent 55%),
                radial-gradient(ellipse at 75% 55%, var(--xray-light) 0%, #3a3a3a 30%, transparent 55%),
                var(--xray-dark);
  }
  .contact-icon {
    position: absolute;
    fill: var(--ink);
  }
  .contact-icon--pin-consult { left: 72px; top: 374px; width: 41px; height: 57px; }
  .contact-icon--pin-postal  { left: 72px; top: 498px; width: 41px; height: 57px; }
  .contact-icon--phone       { left: 617px; top: 380px; width: 44px; height: 44px; }
  .affiliation {
    position: absolute;
    color: var(--ink);
    display: flex;
    align-items: center;
  }
  .affiliation__mark {
    background: var(--ink);
    flex: none;
  }
  .affiliation--college {
    left: 679px;
    top: 532px;
    gap: 8px;
  }
  .affiliation--college .affiliation__mark { width: 40px; height: 72px; }
  .affiliation--college .affiliation__acronym {
    font-size: 30px;
    font-weight: 400;
    line-height: 1;
  }
  .affiliation--college .affiliation__title {
    font-size: 9.5px;
    line-height: 1.35;
    margin-top: 4px;
  }
  .affiliation--association {
    left: 950px;
    top: 494px;
    width: 140px;
    flex-direction: column;
    text-align: center;
  }
  .affiliation--association .affiliation__mark { width: 40px; height: 40px; border-radius: 50%; margin-bottom: 8px; }
  .affiliation--association .affiliation__acronym {
    font-size: 24px;
    font-weight: 400;
    line-height: 1;
  }
  .affiliation--association .affiliation__title {
    font-size: 7.5px;
    line-height: 1.3;
    margin-top: 5px;
    text-transform: uppercase;
  }
</style>
</head>
<body>
  <div class="card">
    <div class="card__band"></div>

    <div class="identity">
      <h1 class="identity__name">Dr Mira Thalen</h1>
      <p class="identity__role">Orthopaedic Hand Surgeon</p>
      <p class="identity__credentials">MBBS BSc (Med), MIntPH (Merit), FCWES (Ortho), FUPelV</p>
    </div>

    <div class="xray" role="img" aria-label="X-ray image of two hands, palms facing forward"></div>

    <svg class="contact-icon contact-icon--pin-consult" viewBox="0 0 24 34" aria-hidden="true">
      <path d="M12 0C5.4 0 0 5.2 0 11.7 0 20 12 34 12 34s12-14 12-22.3C24 5.2 18.6 0 12 0zm0 16.2a4.6 4.6 0 1 1 0-9.2 4.6 4.6 0 0 1 0 9.2z"/>
    </svg>
    <svg class="contact-icon contact-icon--pin-postal" viewBox="0 0 24 34" aria-hidden="true">
      <path d="M12 0C5.4 0 0 5.2 0 11.7 0 20 12 34 12 34s12-14 12-22.3C24 5.2 18.6 0 12 0zm0 16.2a4.6 4.6 0 1 1 0-9.2 4.6 4.6 0 0 1 0 9.2z"/>
    </svg>
    <svg class="contact-icon contact-icon--phone" viewBox="0 0 24 24" aria-hidden="true">
      <path d="M6.6 10.8c1.4 2.8 3.8 5.1 6.6 6.6l2.2-2.2c.3-.3.7-.4 1-.2 1.1.4 2.3.6 3.6.6.6 0 1 .4 1 1V20c0 .6-.4 1-1 1C10.6 21 3 13.4 3 4c0-.6.4-1 1-1h3.5c.6 0 1 .4 1 1 0 1.3.2 2.5.6 3.6.1.3 0 .7-.2 1L6.6 10.8z"/>
    </svg>

    <div class="affiliation affiliation--college">
      <span class="affiliation__mark"></span>
      <div>
        <div class="affiliation__acronym">FCWES</div>
        <div class="affiliation__title">Fellow of the<br>College of Wrist &amp; Extremity Surgeons</div>
      </div>
    </div>

    <div class="affiliation affiliation--association">
      <span class="affiliation__mark"></span>
      <div class="affiliation__acronym">FUPelV</div>
      <div class="affiliation__title">Fellow of the<br>United Pelvic<br>Orthopaedic Association</div>
    </div>
  </div>
</body>
</html>
```